Aerospace Center needs app design

We need a design that would be a creative and innovative look of a simple idea connecting air traffic control situations with sonification.
We would like to see designs that use the elements shown in the short video which are different pads, showing 4 different colors, connecting with a degree and feeling of urgency. The different pads will be movable over screen, similar as to a whiteboard where you can move things around. Each of those pads has 4 different elements that are shown:
- ATC Event (you can chose different setups)
- Select a status (you can chose between Information, Caution and Alert. Color needs to feel more alert from Information to Alert.
- Notes box (you can open the box and write additional text on it)
- Music (you can chose different files. on the right side you can see a small group of notes. When you hover over the notes, music will be played without pressing a play or stop button.
The second video is an overview of music archival program that is connected with the pads.
Look and feel
Each slider illustrates characteristics of the customer's brand and the style your logo design should communicate.

```html
<!DOCTYPE html>
<html lang="en">
<head>
<meta charset="utf-8">
<title>Music Entries – Soundboards</title>
<link href="https://fonts.googleapis.com/css2?family=Poppins:wght@400;500;600;700&display=swap" rel="stylesheet">
<style>
  :root{
    --canvas:#f1f1f4;
    --white:#ffffff;
    --ink:#1e1e2a;
    --muted:#8a8a99;
    --field:#f3f3f5;
    --icon-grey:#c4c4cc;
    --purple:#7b6cf6;
    --purple-soft:#eeecfe;
    --green:#2dcb6b;
    --green-dk:#1e9e51;
    --yellow:#fcd600;
    --yellow-dk:#d8b600;
    --red:#ff0000;
    --red-dk:#c30000;
    --dark:#262626;
    --dark-dk:#444444;
  }
  *{box-sizing:border-box;margin:0;padding:0}
  html,body{width:1200px;height:860px;overflow:hidden}
  body{background:var(--canvas);font-family:"Poppins",sans-serif;color:var(--ink);position:relative}

  /* top bar */
  .topbar{position:absolute;left:0;top:0;width:1200px;height:39px;background:var(--white);box-shadow:0 2px 8px rgba(0,0,0,.04)}
  .brand{position:absolute;left:10px;top:6px;width:24px;text-align:center}
  .brand__mark{display:block;width:10px;height:10px;margin:0 auto 2px;border-radius:50%;background:var(--purple)}
  .brand__name{display:block;font-size:7px;font-weight:700;color:#2d5bd8;line-height:8px}
  .menu-btn{position:absolute;left:46px;top:7px;width:24px;height:24px;border-radius:50%;background:#f2f2f7;display:flex;align-items:center;justify-content:center}
  .page-title{position:absolute;left:84px;top:10px;font-size:12px;font-weight:600}
  .search{position:absolute;left:184px;top:7px;width:642px;height:24px;background:#f5f5f8;border-radius:3px;display:flex;align-items:center;padding-left:10px;gap:7px;font-size:6.5px;color:var(--muted)}
  .round-btn{position:absolute;top:7px;width:24px;height:24px;border-radius:50%;background:#f2f2f7;display:flex;align-items:center;justify-content:center}
  .avatar{position:absolute;left:1077px;top:7px;width:24px;height:24px;border-radius:50%;background:linear-gradient(135deg,#c99a7a,#4a3a3a)}
  .user{position:absolute;left:1106px;top:10px;line-height:9px}
  .user__role{font-size:6px;color:var(--purple);display:block}
  .user__name{font-size:7px;font-weight:500;display:block}

  /* zoom */
  .zoom{position:absolute;left:190px;top:58px;width:49px;text-align:center}
  .zoom__label{font-size:5px;letter-spacing:1.5px;color:var(--purple);display:block;margin-bottom:3px}
  .zoom__track{height:11px;border-radius:2px;background:var(--purple);position:relative}
  .zoom__track::before{content:"";position:absolute;left:19px;top:4px;width:12px;height:3px;border-radius:2px;background:#fff}
  .zoom__track svg{position:absolute;top:3px}

  /* side rail */
  .rail{position:absolute;left:6px;top:136px;width:36px;height:236px;border-radius:18px;background:var(--purple)}
  .rail::after{content:"";position:absolute;right:-4px;top:34px;border:4px solid transparent;border-left-color:var(--purple);border-right:0}
  .rail__item{position:absolute;left:9px;width:18px;height:18px}

  /* soundboard pad */
  .pad{position:absolute;width:167px;border-radius:6px;overflow:hidden;background:var(--c);box-shadow:0 8px 18px rgba(0,0,0,.07)}
  .pad__head{height:36px;display:flex;align-items:center;padding:0 16px 0 19px;color:#fff;font-size:9px;font-weight:600;letter-spacing:.1px}
  .pad__head svg{margin-right:9px}
  .pad__ctrl{margin-left:auto;display:flex;gap:3px}
  .pad__ctrl i{width:10px;height:10px;border-radius:50%;background:var(--cd);display:block}
  .pad__body{padding:0 13px 0 16px}
  .pad__label{display:block;font-size:6.3px;height:9px;line-height:9px;margin:10px 0 4px;color:#fff}
  .field{height:28px;background:var(--white);display:flex;align-items:center;padding:0 10px 0 9px;font-size:8.6px;font-weight:500;gap:9px}
  .field svg.chev{margin-left:auto}
  .field--notes{margin-top:6px}
  .field--open{height:81px;display:block;padding:8px 8px 0 8px}
  .field--open .field__row{display:flex;align-items:center;gap:9px}
  .field__text{font-size:7px;line-height:11.5px;color:#555;font-weight:400;margin-top:13px}
  .pad__foot{position:absolute;left:0;bottom:0;width:100%;height:19px;background:linear-gradient(#f5f5f5,#e7e7e7)}
  .pad__bump{position:absolute;left:59px;top:-26px;width:48px;height:48px;border-radius:50%;background:var(--c)}
  .play{position:absolute;left:66px;top:-19px;width:34px;height:34px;border-radius:50%;background:var(--c);border:2px solid #fff;display:flex;align-items:center;justify-content:center}

  /* light body variant */
  .pad--light{background:var(--white)}
  .pad--light .pad__head{background:var(--c)}
  .pad--light .pad__label{color:var(--ink)}
  .pad--light .field{background:var(--field)}
  .pad--light .pad__foot{background:var(--c)}
  .pad--light .pad__bump{background:var(--white)}
  .pad--light .play{background:var(--white);border-color:var(--c)}
  .pad--light .play svg{stroke:var(--c)}

  .green{--c:var(--green);--cd:var(--green-dk)}
  .yellow{--c:var(--yellow);--cd:var(--yellow-dk)}
  .red{--c:var(--red);--cd:var(--red-dk)}
  .dark{--c:var(--dark);--cd:var(--dark-dk)}

  /* minimized */
  .min-label{position:absolute;left:967px;top:463px;font-size:8.5px;font-weight:600}
  .min-bar{position:absolute;left:963px;top:478px;width:167px;height:35px;border-radius:6px;background:var(--dark);display:flex;align-items:center;padding:0 16px 0 19px;color:#fff;font-size:9px;font-weight:600}
  .min-bar svg{margin-right:9px}
  .min-bar .pad__ctrl i{background:#444}
</style>
</head>
<body>

<svg width="0" height="0" style="position:absolute">
  <defs>
    <symbol id="pin" viewBox="0 0 16 16"><path d="M10 1l5 5-2 1-3 3 .5 3-1.5 1.5-3-3L2 15l-1-1 3.5-4-3-3L3 5.5 6 6l3-3z" fill="#fff"/></symbol>
    <symbol id="chev" viewBox="0 0 10 10"><path d="M2 3.5l3 3 3-3" fill="none" stroke="#222" stroke-width="1.3"/></symbol>
    <symbol id="ico-event" viewBox="0 0 14 14"><g fill="none" stroke="#c4c4cc" stroke-width="1"><rect x="2" y="6" width="10" height="7"/><path d="M4 6V3h6v3M7 1v2"/></g></symbol>
    <symbol id="ico-status" viewBox="0 0 14 14"><g fill="none" stroke="#c4c4cc" stroke-width="1"><rect x="1.5" y="2" width="8" height="10"/><rect x="5" y="5" width="8" height="8"/></g></symbol>
    <symbol id="ico-sound" viewBox="0 0 14 14"><g fill="none" stroke="#c4c4cc" stroke-width="1"><rect x="2" y="2" width="10" height="10" rx="2"/><path d="M5 10V6a2 2 0 014 0v4"/></g></symbol>
    <symbol id="ico-notes" viewBox="0 0 14 14"><g fill="none" stroke="#c4c4cc" stroke-width="1"><rect x="1.5" y="3" width="8" height="10"/><path d="M4 3V1h8v10h-2M3.5 6h4M3.5 8h4M3.5 10h3"/></g></symbol>
    <symbol id="music" viewBox="0 0 20 20"><g fill="none" stroke-width="1.5" stroke-linecap="round"><path d="M6 16V7l8-2v9"/><circle cx="4.5" cy="16" r="1.6"/><circle cx="12.5" cy="14" r="1.6"/><path d="M6 10l8-2M16 2v4M14 4h4"/></g></symbol>
  </defs>
</svg>

<header class="topbar">
  <div class="brand"><span class="brand__mark"></span><span class="brand__name">AERO</span></div>
  <div class="menu-btn"><svg width="10" height="8" viewBox="0 0 10 8"><path d="M0 1h10M0 4h10M0 7h10" stroke="#7b6cf6" stroke-width="1.2"/></svg></div>
  <h1 class="page-title">Music Entries</h1>
  <div class="search"><svg width="8" height="8" viewBox="0 0 10 10"><circle cx="4" cy="4" r="3.2" fill="none" stroke="#333" stroke-width="1.2"/><path d="M6.5 6.5L9 9" stroke="#333" stroke-width="1.2"/></svg>Type your text here..</div>
  <div class="round-btn" style="left:1009px"><svg width="11" height="9" viewBox="0 0 11 9"><rect x=".6" y=".6" width="9.8" height="7.8" rx="1.5" fill="none" stroke="#333"/><path d="M1 1.5l4.5 3.5L10 1.5" fill="none" stroke="#333"/></svg></div>
  <div class="round-btn" style="left:1041px"><svg width="11" height="12" viewBox="0 0 11 12"><path d="M2 9V5.5a3.5 3.5 0 017 0V9l1 1H1zM4.5 11h2" fill="none" stroke="#333"/><circle cx="9" cy="2.5" r="2" fill="#7b6cf6"/></svg></div>
  <div class="avatar" role="img" aria-label="Profile photo of the admin user"></div>
  <div class="user"><span class="user__role">Admin</span><span class="user__name">Lena Hartwig</span></div>
  <div class="round-btn" style="left:1165px"><svg width="12" height="12" viewBox="0 0 12 12"><circle cx="6" cy="6" r="4.8" fill="none" stroke="#333"/><circle cx="6" cy="6" r="2" fill="none" stroke="#333"/></svg></div>
</header>

<div class="zoom">
  <span class="zoom__label">ZOOM</span>
  <div class="zoom__track">
    <svg style="left:4px" width="4" height="5" viewBox="0 0 4 5"><path d="M3 0L0 2.5 3 5z" fill="#fff"/></svg>
    <svg style="right:4px" width="4" height="5" viewBox="0 0 4 5"><path d="M1 0l3 2.5L1 5z" fill="#fff"/></svg>
  </div>
</div>

<nav class="rail">
  <svg class="rail__item" style="top:28px" viewBox="0 0 18 18"><g fill="none" stroke="#fff"><rect x="1" y="1" width="16" height="16"/><path d="M1 6h16M4 9v6M9 9v6M14 9v6"/></g></svg>
  <svg class="rail__item" style="top:61px" viewBox="0 0 18 18"><g fill="none" stroke="#fff" stroke-width="1.3"><rect x="1" y="1" width="6" height="7"/><rect x="10" y="1" width="7" height="6"/><rect x="1" y="11" width="6" height="6"/><rect x="10" y="10" width="7" height="7"/></g></svg>
  <svg class="rail__item" style="top:98px" viewBox="0 0 18 18"><g fill="none" stroke="#fff" stroke-width="1.2"><circle cx="6" cy="11" r="4"/><rect x="9" y="1" width="8" height="6" rx="1"/><path d="M2 17h8"/></g></svg>
  <svg class="rail__item" style="top:135px" viewBox="0 0 18 18"><g fill="none" stroke="#fff" stroke-width="1.2"><rect x="1" y="4" width="12" height="9" rx="1"/><path d="M5 2h12v9M3 15l2-2M4 7h7M4 10h5"/></g></svg>
  <svg class="rail__item" style="top:171px" viewBox="0 0 18 18"><g fill="none" stroke="#fff" stroke-width="1.3"><path d="M7 14V3l7 4-7 2"/><circle cx="4.5" cy="14" r="2.5"/><path d="M11 13h6M11 16h6"/></g></svg>
  <svg class="rail__item" style="top:200px" viewBox="0 0 18 18"><g fill="none" stroke="#fff" stroke-width="1.3"><path d="M11 3V1H2v14l6 2V4l3-1M11 12v3H8M10 8h7M14 5l3 3-3 3"/></g></svg>
</nav>

<!-- top row -->
<section class="pad green" style="left:110px;top:123px;height:270px">
  <div class="pad__head"><svg width="14" height="14"><use href="#pin"/></svg>SOUNDBOARD 1<span class="pad__ctrl"><i></i><i></i></span></div>
  <div class="pad__body">
    <span class="pad__label">Select ATC Event</span>
    <div class="field"><svg width="13" height="13"><use href="#ico-event"/></svg>Landing<svg class="chev" width="9" height="9"><use href="#chev"/></svg></div>
    <span class="pad__label">Select Status Level</span>
    <div class="field"><svg width="13" height="13"><use href="#ico-status"/></svg>1.Information<svg class="chev" width="9" height="9"><use href="#chev"/></svg></div>
    <span class="pad__label">Select Sound File</span>
    <div class="field"><svg width="13" height="13"><use href="#ico-sound"/></svg>Batch Tocatta<svg class="chev" width="9" height="9"><use href="#chev"/></svg></div>
    <div class="field field--notes"><svg width="13" height="13"><use href="#ico-notes"/></svg>Notes<svg class="chev" width="9" height="9"><use href="#chev"/></svg></div>
  </div>
  <div class="pad__foot"><span class="pad__bump"></span><span class="play"><svg width="18" height="18" stroke="#fff"><use href="#music"/></svg></span></div>
</section>

<section class="pad yellow" style="left:333px;top:123px;height:270px">
  <div class="pad__head"><svg width="14" height="14"><use href="#pin"/></svg>SOUNDBOARD 1<span class="pad__ctrl"><i></i><i></i></span></div>
  <div class="pad__body">
    <span class="pad__label">Select ATC Event</span>
    <div class="field"><svg width="13" height="13"><use href="#ico-event"/></svg>Landing<svg class="chev" width="9" height="9"><use href="#chev"/></svg></div>
    <span class="pad__label">Select Status Level</span>
    <div class="field"><svg width="13" height="13"><use href="#ico-status"/></svg>1.Information<svg class="chev" width="9" height="9"><use href="#chev"/></svg></div>
    <span class="pad__label">Select Sound File</span>
    <div class="field"><svg width="13" height="13"><use href="#ico-sound"/></svg>Batch Tocatta<svg class="chev" width="9" height="9"><use href="#chev"/></svg></div>
    <div class="field field--notes"><svg width="13" height="13"><use href="#ico-notes"/></svg>Notes<svg class="chev" width="9" height="9"><use href="#chev"/></svg></div>
  </div>
  <div class="pad__foot"><span class="pad__bump"></span><span class="play"><svg width="18" height="18" stroke="#fff"><use href="#music"/></svg></span></div>
</section>

<section class="pad red" style="left:545px;top:123px;height:270px">
  <div class="pad__head"><svg width="14" height="14"><use href="#pin"/></svg>SOUNDBOARD 1<span class="pad__ctrl"><i></i><i></i></span></div>
  <div class="pad__body">
    <span class="pad__label">Select ATC Event</span>
    <div class="field"><svg width="13" height="13"><use href="#ico-event"/></svg>Landing<svg class="chev" width="9" height="9"><use href="#chev"/></svg></div>
    <span class="pad__label">Select Status Level</span>
    <div class="field"><svg width="13" height="13"><use href="#ico-status"/></svg>1.Information<svg class="chev" width="9" height="9"><use href="#chev"/></svg></div>
    <span class="pad__label">Select Sound File</span>
    <div class="field"><svg width="13" height="13"><use href="#ico-sound"/></svg>Batch Tocatta<svg class="chev" width="9" height="9"><use href="#chev"/></svg></div>
    <div class="field field--notes"><svg width="13" height="13"><use href="#ico-notes"/></svg>Notes<svg class="chev" width="9" height="9"><use href="#chev"/></svg></div>
  </div>
  <div class="pad__foot"><span class="pad__bump"></span><span class="play"><svg width="18" height="18" stroke="#fff"><use href="#music"/></svg></span></div>
</section>

<section class="pad green" style="left:775px;top:123px;height:332px">
  <div class="pad__head"><svg width="14" height="14"><use href="#pin"/></svg>SOUNDBOARD 1<span class="pad__ctrl"><i></i><i></i></span></div>
  <div class="pad__body">
    <span class="pad__label">Select ATC Event</span>
    <div class="field"><svg width="13" height="13"><use href="#ico-event"/></svg>Landing<svg class="chev" width="9" height="9"><use href="#chev"/></svg></div>
    <span class="pad__label">Select Status Level</span>
    <div class="field"><svg width="13" height="13"><use href="#ico-status"/></svg>1.Information<svg class="chev" width="9" height="9"><use href="#chev"/></svg></div>
    <span class="pad__label">Select Sound File</span>
    <div class="field"><svg width="13" height="13"><use href="#ico-sound"/></svg>Batch Tocatta<svg class="chev" width="9" height="9"><use href="#chev"/></svg></div>
    <div class="field field--notes field--open" style="margin-top:10px">
      <div class="field__row"><svg width="13" height="13"><use href="#ico-notes"/></svg>Notes</div>
      <p class="field__text">Sed ut perspiciatis unde o<br>natus error sit voluptatem accusan-<br>tium doloremque laudantium,</p>
    </div>
  </div>
  <div class="pad__foot"><span class="pad__bump"></span><span class="play"><svg width="18" height="18" stroke="#fff"><use href="#music"/></svg></span></div>
</section>

<section class="pad dark" style="left:982px;top:123px;height:270px">
  <div class="pad__head"><svg width="14" height="14"><use href="#pin"/></svg>SOUNDBOARD 1<span class="pad__ctrl"><i></i><i></i></span></div>
  <div class="pad__body">
    <span class="pad__label">Select ATC Event</span>
    <div class="field"><svg width="13" height="13"><use href="#ico-event"/></svg>Landing<svg class="chev" width="9" height="9"><use href="#chev"/></svg></div>
    <span class="pad__label">Select Status Level</span>
    <div class="field"><svg width="13" height="13"><use href="#ico-status"/></svg>1.Information<svg class="chev" width="9" height="9"><use href="#chev"/></svg></div>
    <span class="pad__label">Select Sound File</span>
    <div class="field"><svg width="13" height="13"><use href="#ico-sound"/></svg>Batch Tocatta<svg class="chev" width="9" height="9"><use href="#chev"/></svg></div>
    <div class="field field--notes"><svg width="13" height="13"><use href="#ico-notes"/></svg>Notes<svg class="chev" width="9" height="9"><use href="#chev"/></svg></div>
  </div>
  <div class="pad__foot"><span class="pad__bump"></span><span class="play"><svg width="18" height="18" stroke="#fff"><use href="#music"/></svg></span></div>
</section>

<!-- bottom row -->
<section class="pad pad--light green" style="left:110px;top:520px;height:271px">
  <div class="pad__head"><svg width="14" height="14"><use href="#pin"/></svg>SOUNDBOARD 1<span class="pad__ctrl"><i></i><i></i></span></div>
  <div class="pad__body">
    <span class="pad__label">Select ATC Event</span>
    <div class="field"><svg width="13" height="13"><use href="#ico-event"/></svg>Landing<svg class="chev" width="9" height="9"><use href="#chev"/></svg></div>
    <span class="pad__label">Select Status Level</span>
    <div class="field"><svg width="13" height="13"><use href="#ico-status"/></svg>1.Information<svg class="chev" width="9" height="9"><use href="#chev"/></svg></div>
    <span class="pad__label">Select Sound File</span>
    <div class="field"><svg width="13" height="13"><use href="#ico-sound"/></svg>Batch Tocatta<svg class="chev" width="9" height="9"><use href="#chev"/></svg></div>
    <div class="field field--notes"><svg width="13" height="13"><use href="#ico-notes"/></svg>Notes<svg class="chev" width="9" height="9"><use href="#chev"/></svg></div>
  </div>
  <div class="pad__foot"><span class="pad__bump"></span><span class="play"><svg width="18" height="18"><use href="#music"/></svg></span></div>
</section>

<section class="pad pad--light yellow" style="left:309px;top:520px;height:271px">
  <div class="pad__head"><svg width="14" height="14"><use href="#pin"/></svg>SOUNDBOARD 1<span class="pad__ctrl"><i></i><i></i></span></div>
  <div class="pad__body">
    <span class="pad__label">Select ATC Event</span>
    <div class="field"><svg width="13" height="13"><use href="#ico-event"/></svg>Landing<svg class="chev" width="9" height="9"><use href="#chev"/></svg></div>
    <span class="pad__label">Select Status Level</span>
    <div class="field"><svg width="13" height="13"><use href="#ico-status"/></svg>1.Information<svg class="chev" width="9" height="9"><use href="#chev"/></svg></div>
    <span class="pad__label">Select Sound File</span>
    <div class="field"><svg width="13" height="13"><use href="#ico-sound"/></svg>Batch Tocatta<svg class="chev" width="9" height="9"><use href="#chev"/></svg></div>
    <div class="field field--notes"><svg width="13" height="13"><use href="#ico-notes"/></svg>Notes<svg class="chev" width="9" height="9"><use href="#chev"/></svg></div>
  </div>
  <div class="pad__foot"><span class="pad__bump"></span><span class="play"><svg width="18" height="18"><use href="#music"/></svg></span></div>
</section>

<section class="pad pad--light red" style="left:500px;top:482px;height:271px">
  <div class="pad__head"><svg width="14" height="14"><use href="#pin"/></svg>SOUNDBOARD 1<span class="pad__ctrl"><i></i><i></i></span></div>
  <div class="pad__body">
    <span class="pad__label">Select ATC Event</span>
    <div class="field"><svg width="13" height="13"><use href="#ico-event"/></svg>Landing<svg class="chev" width="9" height="9"><use href="#chev"/></svg></div>
    <span class="pad__label">Select Status Level</span>
    <div class="field"><svg width="13" height="13"><use href="#ico-status"/></svg>1.Information<svg class="chev" width="9" height="9"><use href="#chev"/></svg></div>
    <span class="pad__label">Select Sound File</span>
    <div class="field"><svg width="13" height="13"><use href="#ico-sound"/></svg>Batch Tocatta<svg class="chev" width="9" height="9"><use href="#chev"/></svg></div>
    <div class="field field--notes"><svg width="13" height="13"><use href="#ico-notes"/></svg>Notes<svg class="chev" width="9" height="9"><use href="#chev"/></svg></div>
  </div>
  <div class="pad__foot"><span class="pad__bump"></span><span class="play"><svg width="18" height="18"><use href="#music"/></svg></span></div>
</section>

<section class="pad pad--light dark" style="left:748px;top:490px;height:271px">
  <div class="pad__head"><svg width="14" height="14"><use href="#pin"/></svg>SOUNDBOARD 1<span class="pad__ctrl"><i></i><i></i></span></div>
  <div class="pad__body">
    <span class="pad__label">Select ATC Event</span>
    <div class="field"><svg width="13" height="13"><use href="#ico-event"/></svg>Landing<svg class="chev" width="9" height="9"><use href="#chev"/></svg></div>
    <span class="pad__label">Select Status Level</span>
    <div class="field"><svg width="13" height="13"><use href="#ico-status"/></svg>1.Information<svg class="chev" width="9" height="9"><use href="#chev"/></svg></div>
    <span class="pad__label">Select Sound File</span>
    <div class="field"><svg width="13" height="13"><use href="#ico-sound"/></svg>Batch Tocatta<svg class="chev" width="9" height="9"><use href="#chev"/></svg></div>
    <div class="field field--notes"><svg width="13" height="13"><use href="#ico-notes"/></svg>Notes<svg class="chev" width="9" height="9"><use href="#chev"/></svg></div>
  </div>
  <div class="pad__foot"><span class="pad__bump"></span><span class="play"><svg width="18" height="18"><use href="#music"/></svg></span></div>
</section>

<!-- minimized state -->
<span class="min-label">MINIMIZE</span>
<div class="min-bar"><svg width="14" height="14"><use href="#pin"/></svg>SOUNDBOARD 1<span class="pad__ctrl"><i></i><i></i></span></div>

</body>
</html>
```